New Web Design Project for kids music school

We need a homepage mockup for a kids' music program. Use your creative talent to come up with something visually appeal and professional for this web-site.

More information is provided in the PDF file called HOME. Also included in this file are links to the photos to be used.

Please let me know if you have more questions.

Target Market(s)

parents

Number of Pages Required

1 page

Font styles to use
Sans Serif

```html
<!DOCTYPE html>
<html lang="en">
<head>
<meta charset="utf-8">
<title>Little Notes – Kids Music Programs</title>
<link href="https://fonts.googleapis.com/css2?family=Delius&family=Lato:wght@400;700&family=Nunito:wght@600;700&display=swap" rel="stylesheet">
<style>
:root{
  --ink:#2b2b2b;
  --brand:#2a17b8;
  --brand-deep:#1a08b9;
  --orange:#f7870f;
  --yellow:#fbb312;
  --footer:#eef1fb;
  --footer-bar:#d6e4fb;
  --muted:#3a3a55;
}
*{box-sizing:border-box;margin:0;padding:0}
html,body{width:1200px;height:3241px;overflow:hidden}
body{position:relative;background:#fff;font-family:"Lato",sans-serif;color:var(--ink)}
.abs{position:absolute}
.display{font-family:"Delius",cursive}

/* header */
.site-header{left:0;top:0;width:1200px;height:89px;background:#fff}
.logo{left:146px;top:24px;font-weight:700;font-size:30px;color:var(--brand);display:flex;align-items:center;gap:10px}
.logo-dot{width:16px;height:16px;border-radius:50%;background:var(--yellow)}
.nav{right:98px;top:0;display:flex;height:89px}
.nav a{font-size:17px;color:#444;text-decoration:none;padding:34px 29px 0;position:relative}
.nav a.active{color:var(--brand)}
.nav a.active::before{content:"";position:absolute;left:29px;right:29px;top:0;height:4px;background:var(--brand)}

/* hero */
.hero{left:0;top:89px;width:1200px;height:642px;background:linear-gradient(120deg,#8b5a55,#b94a7a 40%,#4d5a8a 70%,#6f7a9a)}
.hero-badge{left:113px;top:185px;width:398px;height:398px;border-radius:50%;background:rgba(43,16,200,.9);color:#fff;text-align:center;padding-top:116px}
.hero-badge h1{font-family:"Nunito",sans-serif;font-weight:700;font-size:31px;line-height:34px}
.hero-badge p{font-family:"Delius",cursive;font-size:19px;line-height:29px;margin-top:16px}
.arrow{top:350px;width:30px;height:40px}
.hero-curve{left:0;top:640px;width:1200px;height:91px}

/* live music */
.live-photo{left:118px;top:785px;width:478px;height:340px;border-radius:4px;background:linear-gradient(135deg,#c88a4a,#e8d2a8 50%,#8c6a58)}
.live-copy{left:650px;top:800px;width:460px}
.live-copy h2{font-size:40px;line-height:46px;color:var(--brand);font-weight:400}
.live-copy .ages{font-size:26px;margin-top:12px}
.live-copy p{font-size:16px;line-height:26px;margin-top:20px;color:#333}
.btn{display:inline-block;border-radius:30px;font-weight:700;font-size:18px;text-align:center;text-decoration:none}
.btn-orange{left:645px;top:1058px;width:179px;height:52px;line-height:52px;background:var(--orange);color:#fff}

/* program two */
.sparks-photo{left:540px;top:1223px;width:660px;height:525px;background:linear-gradient(120deg,#b83a3a,#e2d2c8 40%,#2f7a4a 65%,#c23a3a)}
.sparks-shape{left:0;top:1223px;width:640px;height:532px}
.sparks-copy{left:133px;top:1325px;width:418px;color:#fff}
.sparks-copy h2{font-size:37px;line-height:37px;font-weight:400}
.sparks-copy .ages{font-size:24px;margin-top:18px}
.sparks-copy p{font-size:15px;line-height:24.5px;margin-top:16px}
.btn-outline{left:134px;top:1604px;width:169px;height:48px;line-height:44px;border:2px solid #fff;color:#fff;font-size:17px}

/* virtual */
.virtual{left:0;top:1755px;width:1200px;height:433px;background:linear-gradient(180deg,#4670d8 0%,#2a40cc 55%,#1608b8 100%);color:#fff;text-align:center}
.virtual h2{font-size:42px;font-weight:400;margin-top:127px}
.virtual p{font-size:18px;line-height:25px;margin-top:14px}
.btn-white{display:inline-block;margin-top:26px;width:190px;height:54px;line-height:54px;background:#fff;color:var(--brand-deep);border-radius:30px;font-size:19px}

/* videos */
.section-title{left:0;width:1200px;text-align:center;font-weight:400}
.videos-title{top:2235px;font-size:35px;color:#1f2a6e}
.thumb{top:2315px;width:344px;height:226px;background:linear-gradient(135deg,#9a8a6a,#d8c8a8 45%,#c64a5a 80%,#3a2a2a)}
.play{left:142px;top:83px;width:60px;height:60px;border-radius:50%;background:#fff}
.play::after{content:"";position:absolute;left:24px;top:18px;border-left:18px solid #222;border-top:12px solid transparent;border-bottom:12px solid transparent}
.divider{left:60px;top:2597px;width:1087px;height:1px;background:#cfcfd8}
.photos-title{top:2630px;font-size:28px;color:#2a46c0}
.photo-tile{top:2693px;width:200px;height:192px}

/* footer */
.footer{left:0;top:2885px;width:1200px;height:290px;background:var(--footer)}
.fcol{top:2948px}
.fcol h4{font-size:17px;font-weight:700;color:#2a3a7a;letter-spacing:.2px;margin-bottom:14px}
.fcol li{list-style:none;font-size:13.5px;color:var(--muted);line-height:33px}
.socials{display:flex;gap:10px}
.social{width:44px;height:44px;border-radius:50%;background:var(--brand-deep)}
.footer-bar{left:0;top:3175px;width:1200px;height:66px;background:var(--footer-bar);text-align:center;font-size:13.5px;color:#444;line-height:66px}
</style>
</head>
<body>

<header class="abs site-header">
  <div class="abs logo"><span>Little Notes</span><span class="logo-dot"></span></div>
  <nav class="abs nav">
    <a class="active" href="#">Home</a><a href="#">About</a><a href="#">Programs</a><a href="#">Videos</a><a href="#">Lessons</a><a href="#">Contact</a>
  </nav>
</header>

<section class="abs hero" role="img" aria-label="Photo of excited children sitting on the floor raising their hands in a music class"></section>
<div class="abs hero-badge">
  <h1>Live Music Education<br>&amp; The Sparks!<br>Performing Program</h1>
  <p>Programs available for kids 3<br>months to 14 years old</p>
</div>
<svg class="abs arrow" style="left:33px" viewBox="0 0 30 40"><path d="M22 4 L8 20 L22 36" fill="none" stroke="#fff" stroke-width="5"/></svg>
<svg class="abs arrow" style="left:1137px" viewBox="0 0 30 40"><path d="M8 4 L22 20 L8 36" fill="none" stroke="#fff" stroke-width="5"/></svg>
<svg class="abs hero-curve" viewBox="0 0 1200 91" preserveAspectRatio="none">
  <path d="M0 91 L0 84 Q600 -40 1200 70 L1200 91 Z" fill="#fff"/>
  <path d="M50 91 Q600 0 1200 78" fill="none" stroke="var(--orange)" stroke-width="4"/>
</svg>

<section>
  <div class="abs live-photo" role="img" aria-label="Photo of toddlers playing with instruments alongside a teacher"></div>
  <div class="abs live-copy">
    <h2 class="display">Live Music Program</h2>
    <div class="ages display">3 mos. - 3 yrs.</div>
    <p>This “mommy &amp; me” style class is a 45-minute live music adventure. Each class has a singer and pianist guiding little ones through 3 boxes of instruments built for their little hands. We use music to teach movement, vocabulary, numbers, letters, confidence and build a love of music.</p>
  </div>
  <a class="abs btn btn-orange" href="#">Learn More</a>
</section>

<section>
  <div class="abs sparks-photo" role="img" aria-label="Photo of children in holiday costumes posing after a performance"></div>
  <svg class="abs sparks-shape" viewBox="0 0 640 532">
    <defs><linearGradient id="sparksGrad" x1="0" y1="0" x2="1" y2="0.3"><stop offset="0" stop-color="#f7870f"/><stop offset="1" stop-color="#fbb312"/></linearGradient></defs>
    <path d="M0 0 H552 Q700 266 552 532 H0 Z" fill="url(#sparksGrad)"/>
  </svg>
  <div class="abs sparks-copy">
    <h2 class="display">SPARKS! Performance Program</h2>
    <div class="ages display">3 - 14 yrs.</div>
    <p>Kids work once a week to put on a show customized for their class. Every child has a solo, lines, and a big part. We have classes for kids ages 3-14. Our mission is confidence and teaching important life skills through theater. All classes perform their show at the end of the session.</p>
  </div>
  <a class="abs btn btn-outline" href="#">Learn More</a>
</section>

<section class="abs virtual" role="img" aria-label="Blue-tinted photo of children dancing in a classroom">
  <h2 class="display">Virtual Music Lessons</h2>
  <p>Augiat in pede Fusce tellus Sed metus augue convallis et vehicula ut pulvinar eu ante<br>Integer orci tellus tristique vitae consequat nec mauris</p>
  <a class="btn btn-white" href="#">Learn More</a>
</section>

<h2 class="abs section-title videos-title display">Our Latest Class Videos</h2>
<div class="abs thumb" style="left:68px" role="img" aria-label="Video thumbnail of a teacher singing in a classroom"><span class="abs play"></span></div>
<div class="abs thumb" style="left:434px" role="img" aria-label="Video thumbnail of a teacher in a classroom"><span class="abs play"></span></div>
<div class="abs thumb" style="left:799px" role="img" aria-label="Video thumbnail of a teacher reading a storybook"><span class="abs play"></span></div>

<div class="abs divider"></div>
<h2 class="abs section-title photos-title display">Follow us on our photo feed</h2>
<div class="abs photo-tile" style="left:0;background:linear-gradient(135deg,#c8a890,#5a7aa8)" role="img" aria-label="Photo of two teachers holding a book"></div>
<div class="abs photo-tile" style="left:200px;background:linear-gradient(135deg,#e8c890,#f0d030)" role="img" aria-label="Photo of a child in a yellow outfit"></div>
<div class="abs photo-tile" style="left:400px;background:linear-gradient(135deg,#7a7a8a,#3a3a4a)" role="img" aria-label="Photo of a teacher on a video screen"></div>
<div class="abs photo-tile" style="left:600px;background:linear-gradient(135deg,#3a4a4a,#8a3a5a)" role="img" aria-label="Photo of a child singing on stage"></div>
<div class="abs photo-tile" style="left:800px;background:linear-gradient(135deg,#c83a6a,#6a5aa8)" role="img" aria-label="Photo of two children hugging"></div>
<div class="abs photo-tile" style="left:1000px;background:linear-gradient(135deg,#4a4a4a,#d87ab0)" role="img" aria-label="Photo of a girl in a pink dress on stage"></div>

<footer>
  <div class="abs footer"></div>
  <div class="abs fcol" style="left:159px"><h4>QUICK LINKS</h4><ul><li>About Us</li><li>Programs</li><li>Blogs</li><li>Contact Us</li></ul></div>
  <div class="abs fcol" style="left:344px"><h4>RESOURCES</h4><ul><li>Our Story</li><li>Videos</li><li>Virtual Music Lessons</li><li>Live Music</li></ul></div>
  <div class="abs fcol" style="left:543px"><h4>CONTACT US</h4><ul><li>14 Maple Grove Rd. Riverton, MA 01999</li><li>(555) 014-2290</li><li>info@littlenotesmusic.com</li></ul></div>
  <div class="abs fcol" style="left:839px"><h4>FOLLOW US</h4>
    <div class="socials"><span class="social" aria-label="Social link 1"></span><span class="social" aria-label="Social link 2"></span><span class="social" aria-label="Social link 3"></span><span class="social" aria-label="Social link 4"></span></div>
  </div>
  <div class="abs footer-bar">© 2020 Company Name&nbsp; All right reserved</div>
</footer>

</body>
</html>
```